Business card design needed with logo

My business is called KVM Solutions & it is targeted towards mobile equipment maintenance in the Mining and civil industry. My work involves maintenance planning and maintenance management plus also supply tradespeople on a labour hire basis. We can provide from basic shut-down machine rebuild plans to complete rebuild services supply plans and labour to anywhere in Australia. I would like to use the colours Black, Red and Grey, I had done a desgin as attached but doesn't really explain what we do and gears don't embroider well onto shirts.
Updates

I also wanted to see the something replace the gears maybe just making the KVM lettering look a bit different or put together differently 

Hello I have extended the deadline by a few extra days as I would like to update details on the front of card, details below & can be put which ever way looks good;

Liam Fenwick
Director
0417263958
KVM@mailnest.com.au
www.kvmsolutions-demo.com.au

On the back of the card I would like to have the below printed;

Capable of providing, but not limited to, across Australia:
- Contract Maintenance Planning.
- Skilled Mobile Maintenance labour hire.
- New machine build specifications. 
- Plant risk assessments and inspections.
- Shut down and rebuild program planning.
- Preventative maintenance tasks, including build of materials lists, creation and review.

Target Market(s)

Contractors and companies that use small and large earthmoving and mining machines

Industry/Entity Type

Business

Contact Information for Business Card

Trading name is KVM Solutions
My name and title is
Liam Fenwick Director
0417 263 958
KVM@mailnest.com.au

Logo Text

KVM

```html
<!DOCTYPE html>
<html lang="en">
<head>
<meta charset="utf-8">
<title>KVM Solutions – Business Card</title>
<link rel="stylesheet" href="https://fonts.googleapis.com/css2?family=Source+Sans+3:wght@400;600&display=swap">
<style>
  :root {
    --stage: #000000;
    --paper: #ffffff;
    --red: #e20a17;
    --grey: #a0a0a0;
    --grey-soft: #adadad;
    --ink: #1a1a1a;
  }
  * { margin: 0; padding: 0; box-sizing: border-box; }
  html, body {
    width: 1200px; height: 849px; overflow: hidden;
    background: var(--stage);
    font-family: "Source Sans 3", sans-serif;
  }
  .stage {
    position: absolute; left: 0; top: 0;
    width: 1169px; height: 827px;
    transform: scale(1.0265); transform-origin: 0 0;
  }
  .card {
    position: absolute; top: 295px;
    height: 236px; border-radius: 10px; overflow: hidden;
  }
  .card--front { left: 143px; width: 412px; background: var(--paper); }
  .card--back  { left: 612px; width: 415px; background: var(--red); }
  .card__shapes { position: absolute; inset: 0; width: 100%; height: 100%; }

  .contact { position: absolute; left: 22px; top: 26px; color: var(--ink); }
  .contact__name { font-size: 16px; font-weight: 400; line-height: 1; }
  .contact__rule { width: 145px; height: 1px; background: var(--red); margin-top: 4px; }
  .contact__title { font-size: 9px; margin-top: 3px; }
  .contact__list { list-style: none; margin-top: 13px; font-size: 10px; }
  .contact__list li { display: flex; align-items: center; height: 16px; }
  .contact__icon { width: 9px; height: 9px; margin-right: 13px; }

  .brand { position: absolute; display: flex; align-items: baseline; white-space: nowrap; }
  .brand__mark { font-size: 54px; font-weight: 400; line-height: 1; letter-spacing: 1px; }
  .brand__name { font-size: 20px; font-weight: 400; margin-left: 10px; }
  .card--front .brand { left: 22px; top: 152px; color: var(--red); }
  .card--back .brand { left: 106px; top: 152px; color: var(--paper); }
</style>
</head>
<body>
<main class="stage">
  <section class="card card--front" aria-label="Card front">
    <svg class="card__shapes" viewBox="0 0 412 236" preserveAspectRatio="none">
      <polygon fill="var(--grey)" points="347,0 412,0 412,236 267,236 378,55"/>
      <polygon fill="var(--red)" points="325,0 347,0 378,55 267,236 244,236 355,55"/>
      <polygon fill="var(--grey-soft)" opacity="0.5" points="330,236 400,236 400,105 345,105 318,150 300,236" role="img" aria-label="Gear graphics in outline"/>
    </svg>
    <div class="contact">
      <p class="contact__name">Liam Fenwick</p>
      <div class="contact__rule"></div>
      <p class="contact__title">Director</p>
      <ul class="contact__list">
        <li>
          <svg class="contact__icon" viewBox="0 0 10 10"><path fill="var(--red)" d="M2 0.5 L3.6 2.6 L2.8 3.6 Q4 6 6.4 7.2 L7.4 6.4 L9.5 8 L8.4 9.5 Q3.5 9 0.5 1.6 Z"/></svg>
          0417 263 958
        </li>
        <li>
          <svg class="contact__icon" viewBox="0 0 10 10"><rect x="0.5" y="2" width="9" height="6.5" rx="1" fill="var(--red)"/><path d="M1 2.5 L5 5.5 L9 2.5" stroke="#fff" stroke-width="0.8" fill="none"/></svg>
          e-mail : KVM@mailnest.com.au
        </li>
      </ul>
    </div>
    <div class="brand">
      <span class="brand__mark">KVM</span>
      <span class="brand__name">KVM Solutions</span>
    </div>
  </section>

  <section class="card card--back" aria-label="Card back">
    <svg class="card__shapes" viewBox="0 0 415 236" preserveAspectRatio="none">
      <polygon fill="var(--grey)" points="0,0 148,0 178,52 68,236 0,236"/>
      <polygon fill="var(--grey-soft)" opacity="0.5" points="4,4 128,4 128,120 72,210 4,210" role="img" aria-label="Gear graphics in outline"/>
    </svg>
    <div class="brand">
      <span class="brand__mark">KVM</span>
      <span class="brand__name">KVM Solutions</span>
    </div>
  </section>
</main>
</body>
</html>
```